family chiropractic health care team needs a modern business card design

Healthcare office with Chiropractors, Physiotherapists, Massage therapists and possibly other practitioners in the future. This is a friendly family office with patients of all ages (and lots of kids) that just moved into a new larger modern office.
Look at the website for photos of the office.
Design for the front and back of a business card required.
Text for the front:
Office logo and name of the office:
Bright Path Wellness Centre
Name of current Practitioner:
Dr. Marten Quovel B.Sc., D.C. Chiropractor
(But please include options to swap out name and title for other practitioners )

address:
218 Farrow Gate
Etobicoke ON.
K2J 6P4
Phone: 416-872-0196 (PATH)
Web site and email:
www.brightpathwellnesscentre.example
brightpathchiro@mailbox.example

2 versions of the back of the card:
1. text below
2. appointment schedule card

Text on back of card:
Chiropractic Card text on back of the card:
There is more to chiropractic than the relief of headaches and back pain! Our primary focus is the integrity of your nerve system, which controls and regulates every cell and tissue of your body. The moving bones of the spinal column can impair this vital communication link between your brain and body. We help improve the function and structure of your spine, reducing nerve system compromise. The result?
Even non-spinal related health problems can show improvement
without drugs
without surgery
regardless of age
for over a century
naturally

Appointment Card info For Back:
Please integrate design elements from the front of the card into an appointment card format.
M Tu W Th F Sat (and a line for writing on beside each one)

```html
<!DOCTYPE html>
<html lang="en">
<head>
<meta charset="utf-8">
<title>Bright Path Wellness Centre – Business Card</title>
<link rel="stylesheet" href="https://fonts.googleapis.com/css2?family=Raleway:wght@400;500;600;700&display=swap">
<style>
  :root {
    --canvas: #ece9e4;
    --card: #2f2f2f;
    --ink: #e4e4e4;
    --ink-soft: #b9b9b9;
    --green: #8dc63f;
    --shadow: rgba(0,0,0,0.22);
  }
  * { margin: 0; padding: 0; box-sizing: border-box; }
  html, body { width: 1200px; height: 871px; overflow: hidden; }
  body {
    background: var(--canvas);
    font-family: "Raleway", sans-serif;
    position: relative;
  }
  .card {
    position: absolute;
    width: 525px;
    height: 300px;
    background: var(--card);
    color: var(--ink);
    box-shadow: 0 10px 24px var(--shadow);
  }
  .card--back { left: 70px; top: 90px; padding: 36px 40px; }
  .card--front { left: 605px; top: 481px; }

  /* back */
  .about { font-size: 12.5px; line-height: 1.45; font-weight: 500; }
  .result-title { margin-top: 16px; font-size: 13px; font-weight: 700; }
  .result-lead { font-size: 12.5px; line-height: 1.45; font-weight: 500; }
  .benefits { list-style: none; font-size: 12.5px; line-height: 1.45; font-weight: 500; }
  .benefits li { display: flex; align-items: center; gap: 7px; }
  .benefits svg { width: 11px; height: 10px; flex: none; }
  .benefits .closing { padding-left: 0; }

  /* front */
  .brand {
    position: absolute;
    left: 40px; top: 95px;
    width: 210px;
    display: flex; flex-direction: column; align-items: center; gap: 14px;
  }
  .brand-dot { width: 58px; height: 58px; border-radius: 50%; background: var(--green); }
  .brand-name {
    color: var(--green);
    font-size: 19px; font-weight: 700;
    text-align: center; line-height: 1.2;
    letter-spacing: 0.02em;
  }
  .practitioner { position: absolute; left: 268px; top: 46px; }
  .practitioner-name { font-size: 21px; font-weight: 500; letter-spacing: 0.01em; }
  .practitioner-title { font-size: 11px; color: var(--ink-soft); margin-top: 4px; font-weight: 500; }

  .contact {
    position: absolute; left: 268px; top: 160px;
    list-style: none; font-size: 11.5px; font-weight: 500; line-height: 1.35;
  }
  .contact li { display: flex; align-items: flex-start; gap: 7px; margin-bottom: 4px; }
  .contact svg { width: 11px; height: 11px; flex: none; margin-top: 2px; fill: var(--green); }
</style>
</head>
<body>

<section class="card card--back" aria-label="Card back">
  <p class="about">There is more to chiropractic than the relief of headaches and back pain! Our primary focus is the integrity of your nerve system, which controls and regulates every cell and tissue of your body. The moving bones of the spinal column can impair this vital communication link between your brain and body. We help improve the function and structure of your spine, reducing nerve system compromise.</p>
  <p class="result-title">The result?</p>
  <p class="result-lead">Even non-spinal related health problems can show improvement</p>
  <ul class="benefits">
    <li><svg viewBox="0 0 12 11"><path fill="#8dc63f" d="M6 10.5 1 5.6A3 3 0 0 1 6 1.8a3 3 0 0 1 5 3.8z"/></svg>without drugs</li>
    <li><svg viewBox="0 0 12 11"><path fill="#8dc63f" d="M6 10.5 1 5.6A3 3 0 0 1 6 1.8a3 3 0 0 1 5 3.8z"/></svg>without surgery</li>
    <li class="closing">regardless of age for over a century naturally!</li>
  </ul>
</section>

<section class="card card--front" aria-label="Card front">
  <div class="brand">
    <span class="brand-dot"></span>
    <span class="brand-name">Bright Path Wellness Centre</span>
  </div>

  <div class="practitioner">
    <h1 class="practitioner-name">Dr. Marten Quovel</h1>
    <p class="practitioner-title">B.Sc., D.C. Chiropractor</p>
  </div>

  <ul class="contact">
    <li>
      <svg viewBox="0 0 12 12"><path d="M6 0a4 4 0 0 0-4 4c0 3 4 8 4 8s4-5 4-8a4 4 0 0 0-4-4zm0 5.6A1.6 1.6 0 1 1 6 2.4a1.6 1.6 0 0 1 0 3.2z"/></svg>
      <span>218 Farrow Gate<br>Etobicoke ON. K2J 6P4</span>
    </li>
    <li>
      <svg viewBox="0 0 12 12"><path d="M2.4 0.5 4.3 2.8 3.2 4.3a7 7 0 0 0 4.5 4.5l1.5-1.1 2.3 1.9-1.2 2A10 10 0 0 1 0.4 1.7z"/></svg>
      <span>416-872-0196 (PATH)</span>
    </li>
    <li>
      <svg viewBox="0 0 12 12"><path d="M0 2h12v8H0zM1 3v.4l5 3.3 5-3.3V3z" fill-rule="evenodd"/></svg>
      <span>brightpathchiro@mailbox.example</span>
    </li>
    <li>
      <svg viewBox="0 0 12 12"><circle cx="6" cy="6" r="5.2" fill="none" stroke="#8dc63f" stroke-width="1.2"/><path d="M0.8 6h10.4M6 0.8c-2.6 3-2.6 7.4 0 10.4M6 0.8c2.6 3 2.6 7.4 0 10.4" fill="none" stroke="#8dc63f" stroke-width="1"/></svg>
      <span>www.brightpathwellnesscentre.example</span>
    </li>
  </ul>
</section>

</body>
</html>
```